hotel's Website

Hotels website redesign for reference pictures, logo etc see http://restwellmarlow.co.uk/

1. 2-3 Special offers on the main page.
2. Booking calender
3. Location Map
4. Picture gallery.
5. Journeyscope reviews.
6. short description
7. Social Media sharing.
8 Phone number and address.

Industry/Entity Type

Hotel

Requirements
Must have
• 1. 2-3 Special offers on the main page.
2. Booking calender
3. Location Map
4. Picture gallery.
5. Journeyscope reviews.
6. short description
7. Social Media sharing.

```html
<!DOCTYPE html>
<html lang="en">
<head>
<meta charset="utf-8">
<title>Restwell Inn Marlow</title>
<link rel="stylesheet" href="https://fonts.googleapis.com/css2?family=Open+Sans:wght@300;400;600;700&display=swap">
<style>
:root{
  --navy:#2e3742;
  --navy-dark:#262e38;
  --yellow:#f2d31b;
  --yellow-dark:#d8b90e;
  --blue:#0c58b3;
  --blue-light:#1a66c2;
  --page:#ececec;
  --text:#333a44;
  --muted:#7a7f86;
  --white:#ffffff;
}
*{box-sizing:border-box;margin:0;padding:0}
html,body{width:1056px;height:1200px;overflow:hidden}
body{font-family:"Open Sans",Arial,sans-serif;background:var(--page);color:var(--text)}
.wrap{width:772px;margin:0 auto;position:relative}

/* header */
.site-header{background:var(--navy);height:74px}
.site-header .wrap{display:flex;justify-content:space-between;align-items:center;height:74px}
.brand{display:flex;align-items:center;gap:10px}
.brand-square{width:44px;height:50px;background:var(--blue);display:block}
.brand-name{color:var(--white);font-weight:600;font-size:15px;padding-right:12px;border-right:1px solid #5b6470;line-height:50px}
.brand-place{color:var(--white);font-size:13px;line-height:1.2}
.brand-place small{display:block;font-size:6px;letter-spacing:1.5px;color:#aab0b8;margin-top:3px}
.contact{text-align:right;font-size:8px;color:#aab0b8;line-height:15px}
.contact b{color:var(--white)}
.contact a{color:var(--yellow);text-decoration:none}

/* nav */
.main-nav{background:var(--yellow);height:40px}
.main-nav .wrap{display:flex;align-items:center;height:40px}
.main-nav a{font-size:11px;color:var(--navy);text-decoration:none;font-weight:600;padding:5px 12px;margin-right:4px}
.main-nav a.active{background:var(--blue);color:var(--white);padding:5px 16px}
.social{margin-left:auto;display:flex;gap:3px}
.social span{width:15px;height:15px;background:var(--navy);display:block}

/* hero */
.hero{height:380px;position:relative;background:linear-gradient(180deg,#4a2c18 0%,#8a5a34 35%,#b48a62 60%,#e9e3dc 78%,#cfc7bd 100%)}
.slide-arrow{position:absolute;top:136px;width:36px;height:70px;background:rgba(200,200,200,.55);display:flex;align-items:center;justify-content:center}
.slide-arrow.prev{left:0}
.slide-arrow.next{right:0}
.booking{position:absolute;left:50%;bottom:0;transform:translateX(-50%);width:772px;height:52px;background:rgba(245,245,245,.82);display:flex;align-items:center}
.booking-label{background:var(--navy);color:var(--white);font-size:16px;font-weight:600;height:52px;line-height:52px;padding-left:18px;width:160px;position:relative}
.booking-label::after{content:"";position:absolute;right:-14px;top:0;border-left:14px solid var(--navy);border-top:26px solid transparent;border-bottom:26px solid transparent}
.date-field{margin-left:30px;width:172px;height:28px;background:#e3ddd6;border:1px solid #cfc6bc;font-size:10px;font-weight:600;color:#555;display:flex;align-items:center;justify-content:space-between;padding:0 8px}
.date-field + .date-field{margin-left:12px}
.check-btn{margin-left:22px;background:var(--blue);color:var(--white);font-weight:700;font-size:11.5px;height:28px;width:172px;display:flex;align-items:center;justify-content:center}

/* offers */
.offers{display:flex;gap:16px;margin-top:44px}
.offer{width:247px;height:148px;position:relative;border:1px solid #d4d4d4;background:#fff;overflow:hidden}
.offer-photo{position:absolute;inset:0}
.offer-band{position:absolute;left:0;right:0;bottom:0;height:70px;text-align:center;line-height:1}
.offer-band strong{display:block;font-size:30px;font-weight:600;padding-top:2px}
.offer-band span{display:block;font-size:10px;font-weight:600;margin-top:3px;line-height:1.25}
.offer.spa .offer-photo{background:linear-gradient(135deg,#d8b092,#f2d9c4 55%,#c89474)}
.offer.spa .offer-band{background:rgba(242,211,27,.92)}
.offer.spa strong{color:var(--white)}
.offer.spa span{color:var(--navy)}
.offer.sunday .offer-photo{background:linear-gradient(135deg,#5a4a3c,#a79c8c 50%,#d8d2c8)}
.offer.sunday .offer-band{background:rgba(46,55,66,.9);color:var(--white)}
.offer.sunday strong{font-size:22px;padding-top:8px}
.offer.nights .offer-photo{background:linear-gradient(180deg,#6b4428,#a77a52 55%,#e8e2da)}
.offer.nights .offer-band{background:rgba(255,255,255,.82);color:var(--blue)}

/* welcome */
.welcome{display:flex;justify-content:space-between;margin-top:78px}
.intro{width:500px}
.intro h1{font-size:25px;font-weight:400;color:var(--blue-light);margin-bottom:6px}
.intro .lead{font-size:13px;font-weight:600;color:var(--text);line-height:19px;margin-bottom:18px}
.intro p{font-size:10px;color:var(--muted);line-height:18px}
.gallery{width:247px;height:170px;position:relative;background:linear-gradient(160deg,#4a3a30,#8d7b6c 45%,#d9d2cb 75%,#a69888);border:1px solid #cfcfcf}
.gallery-title{position:absolute;top:0;left:0;right:0;height:22px;background:rgba(46,55,66,.85);color:var(--white);font-size:10.5px;font-weight:700;text-align:center;line-height:22px}
.gallery-dots{position:absolute;bottom:10px;left:50%;transform:translateX(-50%);background:rgba(46,55,66,.85);border-radius:8px;padding:4px 8px;display:flex;gap:3px}
.gallery-dots i{width:7px;height:7px;border-radius:50%;background:#fff;display:block}
.gallery-dots i.on{background:#889}

/* footer */
.site-footer{position:absolute;left:0;right:0;top:955px;height:245px;background:var(--navy);color:#dfe2e6}
.site-footer .wrap{display:flex;justify-content:space-between;padding-top:36px}
.col{width:224px}
.col h3{color:var(--yellow);font-size:13px;font-weight:400;margin-bottom:16px}
.col p{font-size:9px;line-height:14px}
.partners{list-style:none;margin-top:14px}
.partners li{font-size:8.5px;line-height:15px;color:#aab0b8;padding-left:10px;position:relative}
.partners li::before{content:"";position:absolute;left:0;top:6px;width:3px;height:3px;background:#7a828c}
.partners li.featured{color:var(--white);font-weight:600}
.review-brand{display:flex;align-items:center;gap:8px;margin:22px 0 20px}
.review-brand i{width:30px;height:30px;border-radius:50%;background:var(--white);display:block}
.review-brand b{font-size:21px;font-weight:600;color:var(--white)}
.review-btn{display:block;width:206px;height:30px;background:var(--yellow);color:var(--navy);font-size:10.5px;font-weight:700;text-align:center;line-height:30px}
.map{width:224px;height:122px;background:linear-gradient(135deg,#e4e0d8,#d6d2ca 50%,#ece9e3);border:1px solid #9aa0a8;position:relative}
.map svg{position:absolute;left:104px;top:44px}
.copyright{font-size:7.5px;color:#c4c9cf;margin-top:8px;text-align:right}
</style>
</head>
<body>
<header class="site-header">
  <div class="wrap">
    <div class="brand">
      <span class="brand-square"></span>
      <span class="brand-name">Restwell Inn</span>
      <span class="brand-place">Marlow - Riverside<small>BY HEARTHLINE HOTELS</small></span>
    </div>
    <div class="contact">
      Tel: <b>+44 (0) 16 2851 4420</b> &nbsp;|&nbsp; Fax: <b>+44 (0) 16 2851 4479</b><br>
      12-16 Mill Lane, Marlow SL7 4BT<br>
      <a href="#">stay@restwellmarlow.co.uk</a>
    </div>
  </div>
</header>

<nav class="main-nav">
  <div class="wrap">
    <a class="active" href="#">Home</a>
    <a href="#">Our Rooms</a>
    <a href="#">Attractions</a>
    <a href="#">London Events</a>
    <a href="#">Special Offers</a>
    <a href="#">Photos</a>
    <a href="#">Directions</a>
    <a href="#">Contact</a>
    <div class="social"><span></span><span></span><span></span><span></span><span></span></div>
  </div>
</nav>

<section class="hero" role="img" aria-label="Photo of a warmly lit hotel bedroom with a white bed and lamps">
  <div class="slide-arrow prev"><svg width="12" height="18" viewBox="0 0 12 18"><path d="M10 1 2 9l8 8" fill="none" stroke="#555" stroke-width="2"/></svg></div>
  <div class="slide-arrow next"><svg width="12" height="18" viewBox="0 0 12 18"><path d="M2 1l8 8-8 8" fill="none" stroke="#555" stroke-width="2"/></svg></div>
  <div class="booking">
    <div class="booking-label">BOOK A ROOM</div>
    <div class="date-field">Check In Date:
      <svg width="10" height="10" viewBox="0 0 10 10"><rect x="0.5" y="1.5" width="9" height="8" fill="none" stroke="#b33" /><rect x="0.5" y="1.5" width="9" height="2.5" fill="#b33"/></svg>
    </div>
    <div class="date-field">Check Out Date:
      <svg width="10" height="10" viewBox="0 0 10 10"><rect x="0.5" y="1.5" width="9" height="8" fill="none" stroke="#b33" /><rect x="0.5" y="1.5" width="9" height="2.5" fill="#b33"/></svg>
    </div>
    <div class="check-btn">CHECK AVAILABILITY</div>
  </div>
</section>

<main class="wrap">
  <section class="offers">
    <article class="offer spa">
      <div class="offer-photo" role="img" aria-label="Photo of a couple enjoying a spa massage"></div>
      <div class="offer-band"><strong>25% OFF</strong><span>ON SPA TREATMENTS</span></div>
    </article>
    <article class="offer sunday">
      <div class="offer-photo" role="img" aria-label="Photo of guests dining served by a waiter"></div>
      <div class="offer-band"><strong>SUNDAY SPECIAL</strong><span>Discount up to £10 when you stay with us<br>for the night of Sunday.</span></div>
    </article>
    <article class="offer nights">
      <div class="offer-photo" role="img" aria-label="Photo of a superior suite bedroom"></div>
      <div class="offer-band"><strong>2 NIGHT</strong><span>Accommodation Packages in Superior<br>Suite for 2 Person</span></div>
    </article>
  </section>

  <section class="welcome">
    <div class="intro">
      <h1>Welcome to Restwell Inn Marlow</h1>
      <p class="lead">Enjoy your stay at Restwell Inn Marlow – Riverside and be sure that you've found our best value on the Internet.</p>
      <p>In order to benefit from these special offers we recommend that you visit our Special Offers page on a regular basis to ensure that you are kept up to date on our ever changing programme. This tastefully appointed four storey building is comprised of three attractive Georgian style townhouses – beautifully renovated and continuously maintained to provide comfort as well as stylish decor and useful amenities in all rooms. Our Hotel is a non smoking hotel.</p>
    </div>
    <div class="gallery" role="img" aria-label="Picture gallery slideshow of hotel bedrooms">
      <div class="gallery-title">OUR PICTURE GALLERY</div>
      <div class="gallery-dots"><i></i><i></i><i></i><i class="on"></i><i></i><i></i><i></i><i></i></div>
    </div>
  </section>
</main>

<footer class="site-footer">
  <div class="wrap">
    <div class="col">
      <h3>Partner Hotels</h3>
      <p>This hotel is owned and operated by the Brookvale Hotel Group, please take a look of some of our other hotels below:</p>
      <ul class="partners">
        <li>Elmstead Lodge - Camden Lock</li>
        <li>Elmstead Express - Earls Court</li>
        <li class="featured">Northgate House Hotel</li>
        <li>Snugstay Victoria</li>
        <li>Snugstay Paddington</li>
        <li>Restwell Suites - King's Cross</li>
      </ul>
    </div>
    <div class="col">
      <h3>Journeyscope</h3>
      <p>Stayed with us before? Want to view experiences from our previous guests? Read reviews on our Journeyscope page.</p>
      <div class="review-brand"><i></i><b>journeyscope</b></div>
      <a class="review-btn">View all Journeyscope Review</a>
    </div>
    <div class="col">
      <h3>Our Location</h3>
      <div class="map" role="img" aria-label="Street map showing the hotel location">
        <svg width="16" height="22" viewBox="0 0 16 22"><path d="M8 21C3 14 1 11 1 8a7 7 0 0 1 14 0c0 3-2 6-7 13z" fill="#e0a21a" stroke="#8a5e00"/><circle cx="8" cy="8" r="2.5" fill="#fff"/></svg>
      </div>
      <p class="copyright">© 2013. Restwellmarlow.co.uk &nbsp;|&nbsp; All rights reserved.</p>
    </div>
  </div>
</footer>
</body>
</html>
```